Brochure and Price List
Quiet Willow Body & Beauty Therapies
Because of a problem on their end that delayed the veiling of this project Pexalune has extended my project by 2 days.
Although there are some designers who have withheld their designs because of the veiling problem I don't expect I will need that full amount of time to choose a winner.
I would like to state again that my preference is for a square brochure in booklet form and a price list in rectangular form listing all the treatments with their prices on the front and all the policies on the back. There will be no treatment descriptions required in the booklet.
I will review and respond to every design.
Thank you!
Here are the omitted business details:
Business Name: Quiet Willow Body & Beauty Therapies
My Name and Qualifications: Marisol T. Dunbeck IFA, ITEC, CIBTAC, CIDESCO
Business Telephone: 441-356-8120
Email: roamingrestmd@fernpost.example
Website: www.quietwillowmobile.example
Tag-lines: Island-wide in-home spa treatments
Call today for bookings
Just a query about the folded brochure vs booklet form:
Is the booklet format a really difficult style to pull off? I noticed that no-one has submitted any booklet or separate price list as of yet and I wonder if it's not the best idea for the look I'm going for. Your creative opinions are welcome.
Thanks!
Hello folks!
The administrators were unable to add the information I sent them to the brief. This is one more effort to get the information to you in the form of a Word document. Please view the attached document for further details of the price list and brochure.
Marisol
I see that #11 is using the same tagline as #1; however, since my own script will be used in the final outcome I do not expect that to be an issue. I regard it only as a filler to demonstrate the use of the space. I have asked for the project to be veiled so that designers cannot see each other's work. That should make you all more comfortable.
I have sent more details to the support team for them to add to my brief. Hopefully that will be posted today.
***Please note that I love the look of "dots" stretching between the treatment item and price on the price list.***
For example:
Hot Stones Pedicure.............................................$60
I would love to see the brochure in thin booklet form. This could be a square or rectangle oriented in landscape or portrait position.
I am very taken by the use of rich colour backgrounds in all these designs. They are beautiful. Thank you for thinking to add flowers and water. I love on a semi tropical island, so that depiction is a very accurate impression for my clients.
I will be checking back between massage appointments. Since I don't work behind a desk I don't have access to a computer while I am with a client.
Thanks again for your patience everyone!
Ohhh!!! Are you asking for the actual details of what will be written in the brochure? I'm sorry! I can add that in about 8 hours. I won't have another chance to get to the computer until then. I was mistaken about what the design stage would include. So sorry!
I put up 6 versions of the logo in the brief. Unfortunately, although I have seen some beautiful examples online, I do not own photos of bamboo and stones to show you what I like. I have downloaded some that I do not think would be allowed. That's the difficulty I am having.
where we can find the details for this project...so that i can start designing it..

```html
<!DOCTYPE html>
<html lang="en">
<head>
<meta charset="utf-8">
<title>Quiet Willow Body &amp; Beauty Therapies – Brochure</title>
<link rel="stylesheet" href="https://fonts.googleapis.com/css2?family=Lora:ital,wght@0,600;1,500&family=Open+Sans:wght@400;600&display=swap">
<style>
:root{
  --page:#ffffff;
  --frame:#d6d6d6;
  --forest:#33400f;
  --olive:#56681a;
  --leaf:#8fae2c;
  --lime:#b9d14e;
  --mist:#e3edbc;
  --cream:#f6f3df;
  --amber:#f0a531;
  --stone:#6f6a5c;
  --petal:#d8344f;
  --skin:#e9c9a8;
}
*{box-sizing:border-box;margin:0;padding:0}
html,body{width:1200px;height:1080px;overflow:hidden;background:var(--page)}
body{position:relative;font-family:"Open Sans",Arial,sans-serif;color:var(--cream)}
.canvas-frame{position:absolute;inset:6px;border:1px solid var(--frame)}
.spread{position:absolute;display:flex;box-shadow:0 2px 6px rgba(0,0,0,.18)}
.spread--outside{left:45px;top:52px;width:585px;height:420px}
.spread--inside{left:486px;top:630px;width:669px;height:420px}
.panel{position:relative;height:100%;overflow:hidden}
.spread--outside .panel{width:195px}
.spread--inside .panel{width:223px}
.photo{position:absolute;display:block}
.heading{font-family:"Lora",Georgia,serif;font-weight:600;letter-spacing:.5px}
.script{font-family:"Lora",Georgia,serif;font-style:italic;font-weight:500}
.copy{font-size:7.5px;line-height:1.5}

/* outside: back panel */
.panel--back{background:linear-gradient(180deg,var(--forest) 0%,var(--olive) 70%,var(--forest) 100%);padding:16px 14px}
.brand{display:flex;align-items:center;gap:8px}
.brand__mark{width:22px;height:22px;border-radius:50%;background:var(--lime)}
.brand__name{font-family:"Lora",Georgia,serif;font-weight:600;font-size:17px;color:var(--cream);line-height:1}
.brand__sub{font-size:7px;color:var(--mist);margin:4px 0 0 30px}
.panel--back .heading{color:var(--amber);font-size:11px;text-align:center;margin:16px 0 6px}
.panel--back .copy{margin-bottom:6px;color:var(--mist)}

/* outside: centre panel */
.panel--centre{background:linear-gradient(90deg,var(--olive),var(--leaf) 45%,var(--lime) 55%,var(--olive))}
.about{position:absolute;left:12px;top:82px;width:171px;height:128px;background:rgba(51,64,15,.55);border:1px solid var(--lime);padding:10px;text-align:center}
.about .script{color:var(--amber);font-size:11px;margin-bottom:4px}
.about .copy{color:var(--cream)}
.contact{position:absolute;left:0;bottom:0;width:100%;padding:8px 10px;background:rgba(51,64,15,.85);text-align:center;font-size:7px;line-height:1.5;color:var(--mist)}
.contact strong{display:block;font-weight:600;color:var(--cream);font-size:8px}

/* outside: cover panel */
.panel--cover{background:linear-gradient(180deg,var(--olive),var(--forest))}
.tagline{position:absolute;right:10px;top:20px;width:80px;font-family:"Lora",Georgia,serif;font-style:italic;font-weight:500;font-size:14px;line-height:1.9;color:var(--cream);text-align:center}

/* inside spread */
.spread--inside .panel{background:linear-gradient(180deg,var(--mist),var(--lime) 60%,var(--leaf))}
.spread--inside .script{color:var(--forest);font-size:12px}
.spread--inside .copy{color:var(--forest)}
.block{position:absolute;left:12px;width:199px}
.price-box{position:absolute;left:10px;width:203px;background:rgba(51,64,15,.88);padding:8px 10px;color:var(--cream)}
.price-box .script{color:var(--amber);font-size:10px;margin-bottom:3px}
.row{display:flex;align-items:baseline;font-size:7px;line-height:1.75}
.row__dots{flex:1;border-bottom:1px dotted currentColor;margin:0 3px;transform:translateY(-2px)}
</style>
</head>
<body>
<div class="canvas-frame"></div>

<section class="spread spread--outside" aria-label="Brochure outside">
  <article class="panel panel--back">
    <div class="brand"><span class="brand__mark"></span><span class="brand__name">Quiet Willow</span></div>
    <p class="brand__sub">Body &amp; Beauty Therapies</p>
    <h2 class="heading">SERVICES</h2>
    <p class="copy">Relaxing massage, facials, body wraps and nail care brought to your door anywhere on the island.</p>
    <p class="copy">All treatments use natural oils and professional products chosen for your comfort.</p>
    <h2 class="heading">CANCELLATIONS</h2>
    <p class="copy">Please give 24 hours notice to cancel or change a booking.</p>
    <p class="copy">Late arrivals may shorten your treatment time.</p>
    <div class="photo" role="img" aria-label="Black spa stones with a red flower" style="left:0;bottom:0;width:195px;height:100px;background:linear-gradient(160deg,var(--olive),#2a2a24 60%,var(--stone))"></div>
  </article>

  <article class="panel panel--centre">
    <div class="photo" role="img" aria-label="Strip of spa photos: hands, oils and candles" style="left:0;top:0;width:195px;height:70px;background:linear-gradient(90deg,var(--skin),#c9a57a 50%,var(--amber))"></div>
    <div class="about">
      <p class="script">About Your Therapist</p>
      <p class="copy">Marisol T. Dunbeck IFA, ITEC, CIBTAC, CIDESCO</p>
      <p class="copy">Qualified therapist bringing years of spa experience to your home.</p>
      <p class="copy">Call today for bookings</p>
    </div>
    <div class="photo" role="img" aria-label="Woman receiving hot stone massage with bamboo" style="left:0;top:222px;width:195px;height:130px;background:linear-gradient(180deg,var(--mist),var(--skin) 60%,var(--leaf))"></div>
    <div class="contact"><strong>Quiet Willow Body &amp; Beauty Therapies</strong>441-356-8120<br>roamingrestmd@fernpost.example<br>www.quietwillowmobile.example</div>
  </article>

  <article class="panel panel--cover">
    <div class="photo" role="img" aria-label="Smiling woman relaxing at a spa" style="left:0;top:0;width:110px;height:150px;background:linear-gradient(135deg,var(--skin),#f3e1cc 60%,var(--olive))"></div>
    <p class="tagline">Island-wide<br>in-home<br>spa<br>treatments</p>
    <div class="photo" role="img" aria-label="Pink lotus flower and stacked stones" style="left:0;top:150px;width:195px;height:150px;background:linear-gradient(180deg,#e8d9cf,var(--stone) 70%,var(--olive))"></div>
    <div class="photo" role="img" aria-label="Red flowers on spa stones by water" style="left:0;top:300px;width:195px;height:120px;background:linear-gradient(180deg,var(--petal),var(--forest) 55%,var(--mist))"></div>
  </article>
</section>

<section class="spread spread--inside" aria-label="Brochure inside">
  <article class="panel">
    <div class="photo" role="img" aria-label="Woman enjoying a back massage" style="left:0;top:0;width:223px;height:60px;background:linear-gradient(90deg,var(--skin),#f4e6d6 50%,var(--leaf))"></div>
    <div class="block" style="top:66px">
      <h3 class="script">For the Body</h3>
      <p class="copy">Unwind with treatments designed to ease tension and restore balance.</p>
    </div>
    <div class="photo" role="img" aria-label="Green bamboo stems and leaves" style="left:0;top:120px;width:223px;height:100px;background:linear-gradient(90deg,var(--leaf),var(--mist) 50%,var(--lime))"></div>
    <div class="price-box" style="top:228px">
      <div class="row"><span>Swedish Massage</span><span class="row__dots"></span><span>$80</span></div>
      <div class="row"><span>Deep Tissue Massage</span><span class="row__dots"></span><span>$90</span></div>
      <div class="row"><span>Hot Stones Massage</span><span class="row__dots"></span><span>$95</span></div>
      <div class="row"><span>Body Scrub</span><span class="row__dots"></span><span>$70</span></div>
      <div class="row"><span>Body Wrap</span><span class="row__dots"></span><span>$75</span></div>
      <div class="row"><span>Aromatherapy</span><span class="row__dots"></span><span>$85</span></div>
    </div>
    <div class="photo" role="img" aria-label="Smooth spa stones" style="left:0;bottom:0;width:223px;height:70px;background:linear-gradient(180deg,var(--lime),var(--stone))"></div>
  </article>

  <article class="panel">
    <div class="block" style="top:6px"><h3 class="script">For the Hands &amp; Feet</h3></div>
    <div class="photo" role="img" aria-label="Hands with spa flowers and feet in a soak" style="left:12px;top:28px;width:199px;height:120px;background:linear-gradient(135deg,var(--skin),#f7ead9 50%,var(--amber))"></div>
    <div class="block" style="top:154px"><p class="copy">Pamper tired hands and feet with soothing soaks and care.</p></div>
    <div class="price-box" style="top:180px">
      <div class="row"><span>Manicure</span><span class="row__dots"></span><span>$35</span></div>
      <div class="row"><span>Pedicure</span><span class="row__dots"></span><span>$45</span></div>
      <div class="row"><span>Hot Stones Pedicure</span><span class="row__dots"></span><span>$60</span></div>
      <div class="row"><span>Paraffin Hands</span><span class="row__dots"></span><span>$30</span></div>
    </div>
    <div class="price-box" style="top:268px">
      <p class="script">Combo Packages</p>
      <div class="row"><span>Mani &amp; Pedi</span><span class="row__dots"></span><span>$75</span></div>
      <div class="row"><span>Massage &amp; Facial</span><span class="row__dots"></span><span>$140</span></div>
      <div class="row"><span>Spa Day</span><span class="row__dots"></span><span>$220</span></div>
    </div>
    <div class="photo" role="img" aria-label="Woman relaxing during a facial" style="left:0;bottom:0;width:223px;height:62px;background:linear-gradient(90deg,var(--mist),var(--skin) 60%,var(--leaf))"></div>
  </article>

  <article class="panel">
    <div class="block" style="top:6px;text-align:right"><h3 class="script">Gratifying Therapies</h3></div>
    <div class="photo" role="img" aria-label="Woman receiving a facial treatment" style="left:12px;top:28px;width:90px;height:80px;background:linear-gradient(135deg,var(--skin),#f5e4d2)"></div>
    <div class="price-box" style="top:116px">
      <div class="row"><span>Classic Facial</span><span class="row__dots"></span><span>$65</span></div>
      <div class="row"><span>Deep Cleanse Facial</span><span class="row__dots"></span><span>$80</span></div>
      <div class="row"><span>Eye Treatment</span><span class="row__dots"></span><span>$30</span></div>
      <div class="row"><span>Back Facial</span><span class="row__dots"></span><span>$70</span></div>
      <div class="row"><span>Lash Tint</span><span class="row__dots"></span><span>$20</span></div>
      <div class="row"><span>Brow Shape</span><span class="row__dots"></span><span>$15</span></div>
    </div>
    <div class="price-box" style="top:222px">
      <p class="script">Waxing</p>
      <div class="row"><span>Brow Wax</span><span class="row__dots"></span><span>$15</span></div>
      <div class="row"><span>Lip Wax</span><span class="row__dots"></span><span>$10</span></div>
      <div class="row"><span>Underarm Wax</span><span class="row__dots"></span><span>$20</span></div>
      <div class="row"><span>Half Leg</span><span class="row__dots"></span><span>$35</span></div>
      <div class="row"><span>Full Leg</span><span class="row__dots"></span><span>$55</span></div>
    </div>
    <div class="photo" role="img" aria-label="Stacked stones with bamboo and red flowers" style="left:0;bottom:0;width:223px;height:80px;background:linear-gradient(180deg,var(--leaf),var(--stone) 60%,var(--petal))"></div>
  </article>
</section>
</body>
</html>
```